Record Sales in.. La Jolla | California

We need a CLEAN and MODERN looking flyer for a property. SIMPLE but CLEAN and cutting edge. We would like to use the logo attached at the bottom of the page. We prefer to only have the flyer front and back. If its necessary - we can do 2 pages.

--

Below is the Information/Stats we would like to include:

4318 Heron Court, La Jolla, CA | "The Cedar Loft"
- 4th Highest Sale in History of La Jolla's Highly Desirable Fern Hollow Community
- Recognized Internationally as a "One-of-a-Kind" Architectural Masterpiece
- Featured on Real Estate TV Show "Coastal Prestige Homes"

3814 Vereda Lumo, La Jolla, CA | Marisol Heights
- 2nd Highest Sale Price
- 3rd Highest Price Per S/F since 1997
- Extensive Pre-MLS Marketing. Sold on Day 1 of Listing

Client Testimonials:

4318 Heron Court
"Ned sold my oceanfront home in La Jolla and literally found the 'needle- in-the-hay-stack' cash buyer through his smart and targeted marketing backed by top notch Whitcombe Global Estates. He is an excellent communicator and negotiator and stays the course through thick and thin until a property is sold, while never losing focus on his #1 goal: to make his client happy. Definitely my agent of choice for any future transaction (buy or sell) and he should be yours too."

3814 Vereda Lumo
"We feel so lucky and fortunate to have found Ned. He promised me he would handle our sale from beginning to the end. Not only did Ned keep his promise, he went above & beyond to make sure the transaction stays at its course and time. Ned far exceeded our expectations in the price of the sale. I definitely will recommend Ned to all my family and friends. Thank you, Ned for an amazing experience."

--

Also include the Agents name and Contact Information below our logo:
- Ned Falworth | (858) 555-0172 | Ned@HOMQ-VT.example

Target Market(s)

Luxury Real Estate

Industry/Entity Type

Property

Colors

Designer to choose colors to be used in the design.

Requirements
Nice to have
• Unique & Modern Design

```html
<!DOCTYPE html>
<html lang="en">
<head>
<meta charset="utf-8">
<title>Record Sales in La Jolla – Flyer Front and Back</title>
<link rel="stylesheet" href="https://fonts.googleapis.com/css2?family=Bebas+Neue&family=Lato:wght@300;400;700&display=swap">
<style>
:root{
  --navy:#1a3462;
  --accent:#2f4d8c;
  --ink:#5d5d5d;
  --white:#ffffff;
  --rule:#c9ccd2;
  --quote:#dcdde0;
  --stage:#e9edf1;
  --bar:rgba(20,24,34,.72);
}
*{box-sizing:border-box;margin:0;padding:0}
html,body{width:1200px;height:861px;overflow:hidden;background:var(--stage);font-family:"Lato",sans-serif}
.flyer{position:absolute;top:94px;width:539px;height:697px;background:var(--white);overflow:hidden;box-shadow:0 6px 16px rgba(0,0,0,.22)}
.flyer--front{left:37px}
.flyer--back{left:605px}
.flyer__art{position:absolute;inset:0;width:539px;height:697px}
.flyer__title{position:absolute;left:38px;top:38px;font-family:"Bebas Neue",sans-serif;font-weight:400;font-size:39px;letter-spacing:.2px;color:var(--white);line-height:1;text-transform:uppercase;white-space:nowrap}
.flyer__address{position:absolute;left:38px;top:88px;font-size:16.5px;color:var(--white);line-height:1.25;font-weight:400}
.brand{position:absolute;left:300px;top:66px;width:215px;text-align:center;color:var(--navy);font-size:15px;font-weight:400;line-height:1.3}
.stats{position:absolute;list-style:none;color:var(--ink);font-weight:300;font-size:12px;line-height:14.5px}
.stats li{margin-bottom:14px}
.flyer--front .stats{left:71px;top:178px;width:170px}
.flyer--back .stats{left:61px;top:180px;width:150px}
.flyer--back .stats li{margin-bottom:15px}
.testimonial{position:absolute;color:var(--ink);font-weight:300;font-size:11px;line-height:14px}
.testimonial__label{color:var(--accent);font-size:12px;font-weight:400}
.flyer--front .testimonial{left:285px;top:164px;width:230px}
.flyer--back .testimonial{left:252px;top:164px;width:262px}
.agent{position:absolute;left:0;bottom:19px;height:33px;display:flex;align-items:center;gap:12px;padding-left:41px;padding-right:30px;background:var(--bar);color:var(--white);font-size:13.5px;font-weight:300;white-space:nowrap}
.agent__name{font-weight:700;text-transform:uppercase;letter-spacing:.2px;margin-right:2px}
.agent__item{display:flex;align-items:center;gap:6px}
.agent__portrait{position:absolute;left:54px;top:584px;width:56px;height:66px;border:3px solid var(--white);background:linear-gradient(#d8d8d8,#8d8d8d)}
</style>
</head>
<body>

<section class="flyer flyer--front">
  <svg class="flyer__art" viewBox="0 0 539 697">
    <defs>
      <linearGradient id="frontPhoto" x1="0" y1="0" x2="1" y2="1">
        <stop offset="0" stop-color="#27306a"/>
        <stop offset=".45" stop-color="#4a3a5a"/>
        <stop offset=".75" stop-color="#7a5634"/>
        <stop offset="1" stop-color="#2a2230"/>
      </linearGradient>
      <linearGradient id="frontThumbA" x1="0" y1="0" x2="0" y2="1">
        <stop offset="0" stop-color="#2d5b8f"/><stop offset="1" stop-color="#8a5a32"/>
      </linearGradient>
      <linearGradient id="frontThumbB" x1="0" y1="0" x2="0" y2="1">
        <stop offset="0" stop-color="#d9d3cc"/><stop offset="1" stop-color="#7a6a5c"/>
      </linearGradient>
    </defs>
    <polygon points="0,0 296,0 205,157 0,157" fill="var(--navy)"/>
    <polygon points="0,347 251,388 251,479 518,479 539,528 539,697 0,697" fill="url(#frontPhoto)" role="img" aria-label="Night view of a glass-walled modern home with lit interiors and terrace"/>
    <polygon points="0,330 38,347 0,347" fill="var(--navy)"/>
    <polygon points="539,345 539,450 518,479 500,479" fill="var(--quote)" opacity=".6"/>
    <rect x="251" y="386" width="268" height="93" fill="var(--white)"/>
    <rect x="260" y="388" width="117" height="79" fill="url(#frontThumbA)" role="img" aria-label="Ocean-view deck at sunset"/>
    <rect x="387" y="388" width="117" height="79" fill="url(#frontThumbB)" role="img" aria-label="Glass terrace overlooking the ocean"/>
    <rect x="262" y="168" width="1" height="162" fill="var(--rule)"/>
    <text x="432" y="398" font-family="Bebas Neue,sans-serif" font-size="62" fill="var(--quote)">“ ”</text>
  </svg>

  <h1 class="flyer__title">The Cedar Loft</h1>
  <p class="flyer__address">4318 Heron Court,<br>La Jolla, CA</p>
  <p class="brand">Tidemark Coastal Group<br>Whitcombe Global Estates</p>

  <ul class="stats">
    <li>4th Highest Sale in History of La Jolla's Highly Desirable Fern Hollow Community</li>
    <li>Recognized Internationally as a "One-of-a-Kind" Architectural Masterpiece</li>
    <li>Featured on Real Estate TV Show "Coastal Prestige Homes"</li>
  </ul>

  <div class="testimonial">
    <p class="testimonial__label">Client Testimonial</p>
    <p>Ned sold my oceanfront home in La Jolla and literally found the 'needle- in-the-hay-stack' cash buyer through his smart and targeted marketing backed by top notch Whitcombe Global Estates. He is an excellent communicator and negotiator and stays the course through thick and thin until a property is sold, while never losing focus on his #1 goal: to make his client happy. Definitely my agent of choice for any future transaction (buy or sell) and he should be yours too.</p>
  </div>

  <div class="agent">
    <span class="agent__name">Ned Falworth</span>
    <span class="agent__item"><svg width="10" height="11" viewBox="0 0 10 11"><path d="M3 1 C1 2 1 6 4 9 C6 10.5 8 10.5 9 9 L7.5 7.5 L6 8.3 C4.5 7.3 3.3 5.8 2.8 4.5 L4 3.3 Z" fill="#fff"/></svg>(858) 555-0172</span>
    <span class="agent__item"><svg width="10" height="8" viewBox="0 0 10 8"><rect x=".5" y=".5" width="9" height="7" fill="none" stroke="#fff"/><path d="M.5 .5 L5 4.5 L9.5 .5" fill="none" stroke="#fff"/></svg>Ned@HOMQ-VT.example</span>
  </div>
  <div class="agent__portrait" role="img" aria-label="Agent portrait"></div>
</section>

<section class="flyer flyer--back">
  <svg class="flyer__art" viewBox="0 0 539 697">
    <defs>
      <linearGradient id="backPhoto" x1="0" y1="0" x2="1" y2="1">
        <stop offset="0" stop-color="#9fb8c4"/>
        <stop offset=".4" stop-color="#d9d2c6"/>
        <stop offset=".8" stop-color="#a89a86"/>
        <stop offset="1" stop-color="#7e7262"/>
      </linearGradient>
      <linearGradient id="backThumbSky" x1="0" y1="0" x2="0" y2="1">
        <stop offset="0" stop-color="#5da7d8"/><stop offset="1" stop-color="#8a8f6e"/>
      </linearGradient>
      <linearGradient id="backThumbRoom" x1="0" y1="0" x2="0" y2="1">
        <stop offset="0" stop-color="#d8c7ad"/><stop offset="1" stop-color="#8c5a32"/>
      </linearGradient>
    </defs>
    <polygon points="0,0 295,0 203,157 0,157" fill="var(--navy)"/>
    <polygon points="0,318 200,318 250,340 250,532 512,532 539,560 539,697 0,697" fill="url(#backPhoto)" role="img" aria-label="Bright master bedroom with ocean view windows and sitting area"/>
    <polygon points="0,318 90,318 0,480" fill="var(--navy)"/>
    <polygon points="539,362 539,470 520,532 512,532 512,400" fill="var(--quote)" opacity=".6"/>
    <rect x="250" y="348" width="262" height="184" fill="var(--white)"/>
    <rect x="259" y="356" width="117" height="79" fill="url(#backThumbRoom)" role="img" aria-label="Open kitchen and dining area"/>
    <rect x="385" y="356" width="118" height="79" fill="url(#backThumbSky)" role="img" aria-label="Exterior of a two-story home"/>
    <rect x="259" y="443" width="117" height="79" fill="url(#backThumbSky)" role="img" aria-label="Patio lounge with ocean view"/>
    <rect x="385" y="443" width="118" height="79" fill="url(#backThumbSky)" role="img" aria-label="Outdoor dining deck with ocean view"/>
    <rect x="227" y="168" width="1" height="146" fill="var(--rule)"/>
    <text x="428" y="360" font-family="Bebas Neue,sans-serif" font-size="62" fill="var(--quote)">“ ”</text>
  </svg>

  <h1 class="flyer__title">Marisol Heights</h1>
  <p class="flyer__address">3814 Vereda Lumo,<br>La Jolla, CA</p>
  <p class="brand">Tidemark Coastal Group<br>Whitcombe Global Estates</p>

  <ul class="stats">
    <li>2nd Highest Sale Price</li>
    <li>3rd Highest Price Per S/F since 1997</li>
    <li>Extensive Pre-MLS Marketing. Sold on Day 1 of Listing</li>
  </ul>

  <div class="testimonial">
    <p class="testimonial__label">Client Testimonial</p>
    <p>"We feel so lucky and fortunate to have found Ned. He promised me he would handle our sale from beginning to the end. Not only did Ned keep his promise, he went above &amp; beyond to make sure the transaction stays at its course and time. Ned far exceeded our expectations in the price of the sale. I definitely will recommend Ned to all my family and friends. Thank you, Ned for an amazing experience."</p>
  </div>

  <div class="agent">
    <span class="agent__name">Ned Falworth</span>
    <span class="agent__item"><svg width="10" height="11" viewBox="0 0 10 11"><path d="M3 1 C1 2 1 6 4 9 C6 10.5 8 10.5 9 9 L7.5 7.5 L6 8.3 C4.5 7.3 3.3 5.8 2.8 4.5 L4 3.3 Z" fill="#fff"/></svg>(858) 555-0172</span>
    <span class="agent__item"><svg width="10" height="8" viewBox="0 0 10 8"><rect x=".5" y=".5" width="9" height="7" fill="none" stroke="#fff"/><path d="M.5 .5 L5 4.5 L9.5 .5" fill="none" stroke="#fff"/></svg>Ned@HOMQ-VT.example</span>
  </div>
  <div class="agent__portrait" role="img" aria-label="Agent portrait"></div>
</section>

</body>
</html>
```